Q.R. Bright Desk Store

The design is for eCommerce home page but I would like it to complement this site: http://www.qrbrightdesksystems.com/ but... it should also have independence as a standalone site.

The best design will be able to effectively mix corporate with a high quality small business consumer feel. It should be completely custom design, not a template look or feel. I want the users to get the feeling that this is the place to go for buying tech for business. We sell the same products as Vantrel.

You can be creative as you wish, as long as the elements of a great eCommerce site are present.

I would like your 'design' to blow these away:
http://www.buying.zorvex.com/
mivoland.com
http://www.vantrel.com/

Here are references:
Call to action
http://trabelwise.com/us/blog/48173-seven-tips-for-designing-an-effective-ecommerce-call-to-action

Effective Ecommerce design
http://www.plov.com/ss/7-tips-for-effective-e-commerce#0

91 points of ecommerce
http://dreb.com/blog/holygrail-of-ecommerce-conversion-optimization-91-points-checklist

UPDATE 07/11/2013:

Please look at the category sample png files. I see already many people are using the main menu from qrbrightdesksystems.com and I do not mind your creativiety, but this is an eCommerce store and people need a menu to get to the categories and/or product types. I don't want to limit anyone creativity by the png samples. I'm also not using them to show I like them in any particular way or form, just that it's needed, whether it's a button (dropdown of course) that says 'Categories' or 'Products, whether it an accordion, horizontal or vertical.

Thanks

UPDATE 07/12/2013:

Please find other use of space that has been used for About Us paragraph (if you've added it to the page). About Us should have it's own page and the purpose of the design should be to sell products (and some services as products). Please put a link or some other creative method to lead users to the About Us page.

Reason: I've raised the award, including 1st, 2nd, and 3rd place and participation payments so I will also extend 7 days. Thanks!

I've updated the product brief. Please scroll down to where it says: UPDATE 07/11/2013

Thanks!

UPDATE 07/12/2013:

Please find other use of space that has been used for About Us paragraph (if you've added it to the page).  About Us should have it's own page and the purpose of the design should be to sell products (and some services as products). Please put a link or some other creative method to lead users to the About Us page if you must but not on the real estate of the page.

Thanks!

Added updates to the brief 7/14/2013.

Thanks!

The voting is in and the project is complete.  Thanks everyone for joining, all of those who participated are truly amazingly talented. But, there were only 3 prizes.  I will be having further projects down the line to develop other pages to this site after the initial implementation is completed.  I truly would like to have you all back. 

- Thank you.

Target Market(s)

corporate decision-makers AND small business consumers

Industry/Entity Type

Small Business

Requirements
Must have
• Call to action.
Openness (non-clutter).

These elements:
Search box
Logo
Tagline
Telephone number
Contact details
Address
My account / sign in
Shopping basket / checkout link
Latest offers
Promotional area
Email sign up
Delivery information
About us
Link to press office / corporate site
Terms and conditions
Sitemap for the footer.
Delivery offers: free
Personalized recommendations
Social media links
Accepted payment methods
Link to blog or community section
Change language / country

http://freshnotesblog.kelvarant.com/sales-leads-landing-page/

UPDATE 07/14/2013
Category Menu. This can be a dropdown, horizontal, vertical, etc. But shoppers need to know how to get to the products they want to buy.
Nice to have
• Trustmarks
Blog/Blog link

UPDATE 07/12/2013:
Make the footer useful.

UPDATE 07/14/2013 (Suggestions of elements to differentiate your designs)

-Quick Shop: A quick buy module/section: Where a user can put in a SKU number or Model number to quickly add the product to their shopping cart.

-Featured
-Best Sellers
-Specials
-Trending Tags/Tag Cloud
- Activity Stream
- Cross Sell/ Up Sell
- Testimonial
- Social Network Feed
- Live Help
- Feedback/Support/Contact Tab
- Show logged in user (i.e. Welcome, Mark Pell)
Should not have
• The design SHOULD NOT be generic like this:

http://www.artflock.com/design/52392
http://www.pelicanvault.com/

The page should not feel over cluttered. It should not have low quality icons or design elements. Navigation should not be hard to discover or confusing.

```html
<!DOCTYPE html>
<html lang="en">
<head>
<meta charset="utf-8">
<title>Q.R. Bright Desk Store</title>
<link href="https://fonts.googleapis.com/css2?family=Open+Sans:ital,wght@0,400;0,600;0,700;0,800;1,400&display=swap" rel="stylesheet">
<style>
:root{
  --navy:#0d3c7a;
  --blue:#1d5fb4;
  --blue-light:#2b78d0;
  --orange:#f26b1d;
  --text:#333;
  --muted:#777;
  --line:#d6dbe1;
  --page:#eef1f4;
  --panel:#f5f6f8;
  --white:#fff;
}
*{box-sizing:border-box;margin:0;padding:0}
html,body{width:758px;height:1200px;overflow:hidden}
body{background:var(--page);font-family:"Open Sans",Arial,sans-serif;color:var(--text);font-size:9px}
.wrap{width:622px;margin:0 auto;position:relative}
a{color:inherit;text-decoration:none}

.topbar{height:20px;display:flex;justify-content:flex-end;align-items:center;gap:8px;font-size:7.5px;color:#555}
.topbar span+span::before{content:"|";margin-right:8px;color:#aaa}

.header{height:72px;display:flex;align-items:center;justify-content:space-between}
.brand{display:flex;align-items:center;gap:8px}
.brand-dot{width:34px;height:34px;border-radius:50%;background:var(--blue)}
.brand-name{font-size:18px;font-weight:800;color:var(--navy);line-height:1;letter-spacing:.3px}
.search{display:flex;align-items:center;height:22px;border:1px solid var(--line);background:var(--white);width:260px}
.search input{flex:1;border:0;height:100%;padding:0 6px;font:inherit;font-size:8px}
.search .cat{height:100%;padding:0 8px;border-left:1px solid var(--line);display:flex;align-items:center;gap:4px;color:#555;font-size:8px}
.search button{height:100%;background:var(--blue);color:#fff;border:0;font:700 8px "Open Sans",sans-serif;padding:0 12px}

.nav{height:22px;background:var(--navy);display:flex;align-items:stretch}
.nav a{color:#fff;font-size:8px;font-weight:600;padding:0 12px;display:flex;align-items:center}
.nav a.active{background:var(--blue-light)}

.hero{height:250px;margin-top:2px;background:linear-gradient(90deg,#f7f8fa 0%,#e7ebef 55%,#d5dce3 100%);position:relative;overflow:hidden}
.hero-copy{position:absolute;left:20px;top:44px}
.hero-title{color:var(--orange);font-size:24px;font-weight:800;line-height:1.1}
.hero-lead{color:var(--navy);font-size:17px;line-height:1.3;margin-top:6px}
.hero-lead b{font-weight:700}
.btn-learn{display:inline-block;margin-top:16px;background:var(--orange);color:#fff;font-size:9px;font-weight:700;padding:6px 12px;border-radius:2px}
.dots{position:absolute;left:20px;bottom:24px;display:flex;gap:5px}
.dots i{width:8px;height:8px;border-radius:50%;background:#888}
.dots i:first-child{background:var(--orange)}
.hero-photo{position:absolute;right:0;top:0;width:220px;height:250px;background:linear-gradient(180deg,#cfd6dd,#9aa6b2)}

.main{display:flex;gap:14px;margin-top:8px}
.products{width:496px}
.section-head{height:24px;background:linear-gradient(#fafbfc,#e6e9ed);border:1px solid var(--line);font-weight:700;font-size:9px;padding:0 10px;display:flex;align-items:center}
.product-row{display:flex;gap:10px;padding:10px 8px 16px;background:var(--white);border:1px solid var(--line);border-top:0;margin-bottom:8px}
.card{flex:1}
.card-img{height:72px;background:linear-gradient(#f0f2f5,#c9d0d7);margin-bottom:6px}
.card p{font-size:7.5px;color:var(--muted);line-height:1.35}
.price{color:var(--orange);font-size:12px;font-weight:700;margin:4px 0}
.actions{display:flex;gap:4px}
.btn-buy,.btn-details{display:flex;align-items:center;gap:3px;font-size:7px;font-weight:700;height:16px;padding:0 6px;border-radius:2px}
.btn-buy{background:var(--blue);color:#fff}
.btn-details{background:#eef1f5;border:1px solid var(--line);color:var(--navy)}
.promo{width:112px;height:432px;background:linear-gradient(180deg,#f6a623 0%,#f08a1a 50%,#2f5d9e 62%,#dfe5ec 100%)}

.testimonials{margin-top:6px}
.testimonials h2{color:var(--orange);font-size:14px;font-weight:700;margin-bottom:8px}
.t-row{display:flex;gap:14px}
.t-card{flex:1;background:var(--white);border:1px solid var(--line);padding:10px;display:flex;gap:10px;height:96px}
.avatar{width:44px;height:44px;flex:none;background:#b8c0c8}
.t-card blockquote{font-size:7.5px;color:var(--muted);line-height:1.4}
.t-card cite{display:block;margin-top:6px;font-style:normal;font-size:7.5px;color:var(--navy);font-weight:700}

.footer-links{margin-top:14px;height:20px;background:var(--navy);color:#fff;font-size:7.5px}
.footer-links .wrap{display:flex;justify-content:space-between;align-items:center;height:20px}
.footer-links nav{display:flex;gap:14px}
.footer{background:#e2e6ea;height:210px;padding-top:12px}
.footer-top{display:flex;justify-content:space-between;align-items:center;height:30px}
.socials{display:flex;gap:6px}
.socials i{width:20px;height:20px;background:var(--blue);display:block}
.socials i:nth-child(2){background:#3aa3d9}
.socials i:nth-child(3){background:#c4302b}
.footer .brand-dot{width:24px;height:24px}
.footer .brand-name{font-size:13px}
.cols{display:flex;justify-content:space-between;margin-top:12px}
.col h4{color:var(--orange);font-size:8.5px;font-weight:700;margin-bottom:5px}
.col li{list-style:none;font-size:7.5px;color:#444;line-height:1.55}
.cards{display:grid;grid-template-columns:repeat(3,26px);gap:4px}
.cards i{height:16px;background:#fff;border:1px solid var(--line);display:block}
.contact .phone{font-size:10px;font-weight:700;color:var(--navy)}
.contact p{font-size:7.5px;line-height:1.5;color:#444}
.copyright{margin-top:14px;font-size:7px;color:#666}
</style>
</head>
<body>
<div class="wrap">
  <div class="topbar"><span>Shop</span><span>My Account</span><span>Checkout</span><span>My Shopping</span><span>Cart 0 items</span></div>
  <header class="header">
    <div class="brand"><span class="brand-dot"></span><span class="brand-name">Q.R. BRIGHT DESK</span></div>
    <form class="search">
      <input type="text" aria-label="Search">
      <span class="cat">Categories
        <svg width="6" height="4" viewBox="0 0 6 4"><path d="M0 0h6L3 4z" fill="#666"/></svg></span>
      <button type="button">SEARCH</button>
    </form>
  </header>
  <nav class="nav">
    <a class="active" href="#">Home</a><a href="#">Small Business</a><a href="#">Latest offers</a><a href="#">Enterprise</a><a href="#">Non Profit</a><a href="#">Contact Us</a>
  </nav>

  <section class="hero">
    <div class="hero-copy">
      <div class="hero-title">Q.R. BRIGHT DESK</div>
      <div class="hero-lead">Should you <b>CHOOSE TO HAVE</b><br>A customized greeting on your<br><b>ACCOUNT, WE WILL NOT .</b></div>
      <a class="btn-learn" href="#">Learn More ›</a>
    </div>
    <div class="dots"><i></i><i></i><i></i><i></i></div>
    <div class="hero-photo" role="img" aria-label="Photo of a smiling businesswoman in an office"></div>
  </section>

  <div class="main">
    <div class="products">
      <div class="section-head">Products with the highest change in sales rank over the past 24 hours</div>
      <div class="product-row">
        <div class="card"><div class="card-img" role="img" aria-label="Product photo of a video camcorder"></div><p>simply dummy text of the printing and typesetting industry.</p><div class="price">$45.00</div><div class="actions"><a class="btn-buy" href="#"><svg width="8" height="7" viewBox="0 0 8 7"><path d="M0 0h1.5l1 4h4l1-3H2.3" fill="none" stroke="#fff" stroke-width=".9"/><circle cx="3" cy="6" r=".7" fill="#fff"/><circle cx="6" cy="6" r=".7" fill="#fff"/></svg>BUY NOW</a><a class="btn-details" href="#">DETAILS</a></div></div>
        <div class="card"><div class="card-img" role="img" aria-label="Product photo of a laptop"></div><p>simply dummy text of the printing and typesetting industry.</p><div class="price">$45.00</div><div class="actions"><a class="btn-buy" href="#"><svg width="8" height="7" viewBox="0 0 8 7"><path d="M0 0h1.5l1 4h4l1-3H2.3" fill="none" stroke="#fff" stroke-width=".9"/><circle cx="3" cy="6" r=".7" fill="#fff"/><circle cx="6" cy="6" r=".7" fill="#fff"/></svg>BUY NOW</a><a class="btn-details" href="#">DETAILS</a></div></div>
        <div class="card"><div class="card-img" role="img" aria-label="Product photo of an office printer"></div><p>simply dummy text of the printing and typesetting industry.</p><div class="price">$45.00</div><div class="actions"><a class="btn-buy" href="#"><svg width="8" height="7" viewBox="0 0 8 7"><path d="M0 0h1.5l1 4h4l1-3H2.3" fill="none" stroke="#fff" stroke-width=".9"/><circle cx="3" cy="6" r=".7" fill="#fff"/><circle cx="6" cy="6" r=".7" fill="#fff"/></svg>BUY NOW</a><a class="btn-details" href="#">DETAILS</a></div></div>
      </div>
      <div class="section-head">Products with the highest change in sales rank over the past 24 hours</div>
      <div class="product-row">
        <div class="card"><div class="card-img" role="img" aria-label="Product photo of a rack server"></div><p>simply dummy text of the printing and typesetting industry.</p><div class="price">$45.00</div><div class="actions"><a class="btn-buy" href="#"><svg width="8" height="7" viewBox="0 0 8 7"><path d="M0 0h1.5l1 4h4l1-3H2.3" fill="none" stroke="#fff" stroke-width=".9"/><circle cx="3" cy="6" r=".7" fill="#fff"/><circle cx="6" cy="6" r=".7" fill="#fff"/></svg>BUY NOW</a><a class="btn-details" href="#">DETAILS</a></div></div>
        <div class="card"><div class="card-img" role="img" aria-label="Product photo of an office desk phone"></div><p>simply dummy text of the printing and typesetting industry.</p><div class="price">$45.00</div><div class="actions"><a class="btn-buy" href="#"><svg width="8" height="7" viewBox="0 0 8 7"><path d="M0 0h1.5l1 4h4l1-3H2.3" fill="none" stroke="#fff" stroke-width=".9"/><circle cx="3" cy="6" r=".7" fill="#fff"/><circle cx="6" cy="6" r=".7" fill="#fff"/></svg>BUY NOW</a><a class="btn-details" href="#">DETAILS</a></div></div>
        <div class="card"><div class="card-img" role="img" aria-label="Product photo of a network storage unit"></div><p>simply dummy text of the printing and typesetting industry.</p><div class="price">$45.00</div><div class="actions"><a class="btn-buy" href="#"><svg width="8" height="7" viewBox="0 0 8 7"><path d="M0 0h1.5l1 4h4l1-3H2.3" fill="none" stroke="#fff" stroke-width=".9"/><circle cx="3" cy="6" r=".7" fill="#fff"/><circle cx="6" cy="6" r=".7" fill="#fff"/></svg>BUY NOW</a><a class="btn-details" href="#">DETAILS</a></div></div>
      </div>
    </div>
    <aside class="promo" role="img" aria-label="Vertical promotional banner with illustrated lettering and a product shot"></aside>
  </div>

  <section class="testimonials">
    <h2>Our Testimonials</h2>
    <div class="t-row">
      <div class="t-card"><div class="avatar" role="img" aria-label="Customer portrait"></div><div><blockquote>"Ordering was quick and the team helped us choose the right laptops for our whole office. Delivery arrived early and setup support was friendly and clear from start to finish."</blockquote><cite>Lena Marsh - Owner of Tidewell Bakery</cite></div></div>
      <div class="t-card"><div class="avatar" role="img" aria-label="Customer portrait"></div><div><blockquote>"Great prices on printers and networking gear. Their account managers answer the phone fast and always follow up, which matters a lot to a small business like ours."</blockquote><cite>Omar Finch - Founder of Grayline Studio</cite></div></div>
    </div>
  </section>
</div>

<div class="footer-links">
  <div class="wrap">
    <nav><a href="#">Site Map</a><a href="#">New Items</a><a href="#">Advanced Search</a><a href="#">Orders and Returns</a><a href="#">Contact Us</a></nav>
    <nav><a href="#">Custom Link</a><a href="#">About Us</a><a href="#">Customer Service</a></nav>
  </div>
</div>
<footer class="footer">
  <div class="wrap">
    <div class="footer-top">
      <div class="socials" aria-label="Social media links"><i></i><i></i><i></i></div>
      <div class="brand"><span class="brand-dot"></span><span class="brand-name">Q.R. BRIGHT DESK</span></div>
    </div>
    <div class="cols">
      <div class="col"><h4>Customer Service</h4><ul><li>Delivery</li><li>Shipping Methods</li><li>Payment</li><li>Returns &amp; Refunds</li><li>Customers</li></ul></div>
      <div class="col"><h4>What's in Store</h4><ul><li>Stores</li><li>Map</li><li>Products A-Z</li><li>Sale</li><li>Buy a Gift Card</li></ul></div>
      <div class="col"><h4>Other Sites</h4><ul><li>Second Site</li><li>Fan Page</li><li>News Feed</li><li>Photo Board</li><li>Video Channel</li></ul></div>
      <div class="col"><h4>Easy payment</h4><div class="cards" aria-label="Accepted payment methods"><i></i><i></i><i></i><i></i><i></i><i></i></div></div>
      <div class="col contact"><h4>Contact us</h4><div class="phone">+001 (000) 555 274</div><p>Q.R. Bright Desk Store<br>48 Harbor Lane, Suite 12<br>Fairview, CA 90210<br>info@qrbrightdesksystems.com</p></div>
    </div>
    <div class="copyright">Copyright © 2013 Q.R. Bright Desk Store. All Rights Reserved</div>
  </div>
</footer>
</body>
</html>
```